I need a business card for myself, being a proprietor of a funeral parlor based in Manila. I'd like the card to have either of the following:
White Font on Black Background
or
Black Font on White Background
No logo is needed however I will appreciate any efforts to show a symbol of eternal happiness, aptly designed with above mentioned colors in mind.
Company name, address and contact on the lower right corner.
Logo or symbol anywhere.
Quillstone Funeral Services
+639174826351
darvik4521@pelmora.com
corner of Brisco Avenue and Velhurst Street
Makati City, Philippines
Thank you.
Update: Please include a small dove in your design. You are free to choose where you would like it on the card.

```html
<!DOCTYPE html>
<html lang="en">
<head>
<meta charset="utf-8">
<title>Quillstone Funeral Services – Business Card</title>
<link href="https://fonts.googleapis.com/css2?family=Questrial&display=swap" rel="stylesheet">
<style>
  :root {
    --page: #e9e6e2;
    --card: #0a0a0a;
    --card-edge: #1a1a1a;
    --ink: #e8e8e8;
    --ink-soft: #cfcfcf;
    --dove-tone: #bdbdbd;
  }
  * { margin: 0; padding: 0; box-sizing: border-box; }
  html, body {
    width: 1200px;
    height: 671px;
    overflow: hidden;
    background: var(--page);
    font-family: "Questrial", "Century Gothic", sans-serif;
  }
  .canvas {
    width: 1200px;
    height: 671px;
    display: flex;
    align-items: center;
    justify-content: center;
  }
  .business-card {
    position: relative;
    width: 900px;
    height: 514px;
    background: var(--card);
    border: 1px solid var(--card-edge);
    box-shadow: 0 10px 30px rgba(0, 0, 0, 0.25);
    color: var(--ink);
  }
  .symbol-dove {
    position: absolute;
    left: 120px;
    top: 110px;
    width: 110px;
    height: 74px;
    background: radial-gradient(ellipse at center, var(--dove-tone) 0%, rgba(189,189,189,0.35) 55%, rgba(10,10,10,0) 75%);
  }
  .company-name {
    position: absolute;
    left: 80px;
    top: 200px;
    color: var(--ink);
    font-weight: 400;
  }
  .company-name .name-main {
    display: block;
    font-size: 54px;
    line-height: 1;
    letter-spacing: 0.5px;
  }
  .company-name .name-sub {
    display: block;
    font-size: 26px;
    line-height: 1.3;
    margin-top: 6px;
    padding-left: 40px;
  }
  .contact-block {
    position: absolute;
    right: 60px;
    top: 250px;
    text-align: right;
    color: var(--ink-soft);
    font-size: 19px;
    line-height: 1.55;
  }
  .contact-line {
    display: flex;
    justify-content: flex-end;
    align-items: center;
    gap: 10px;
  }
  .contact-line svg {
    width: 16px;
    height: 16px;
    fill: var(--ink-soft);
    flex: none;
  }
  .contact-line .icon-spacer { width: 16px; flex: none; }
  .contact-address { margin-top: 18px; }
</style>
</head>
<body>
<main class="canvas">
  <article class="business-card">
    <div class="symbol-dove" role="img" aria-label="Small white dove carrying an olive branch, symbol of peace and eternal rest"></div>

    <h1 class="company-name">
      <span class="name-main">Quillstone</span>
      <span class="name-sub">Funeral Services</span>
    </h1>

    <address class="contact-block">
      <div class="contact-line">
        <span>+639174826351</span>
        <svg viewBox="0 0 16 16" aria-hidden="true"><path d="M2 5c0-2 3-3 6-3s6 1 6 3v1h-3V5H5v1H2z M4 7h8l2 6H2z M8 8.5a2 2 0 1 0 0 4a2 2 0 1 0 0-4z"/></svg>
      </div>
      <div class="contact-line">
        <span>darvik4521@pelmora.com</span>
        <svg viewBox="0 0 16 16" aria-hidden="true"><path d="M1 3h14v10H1z M2 4.2v.4l6 4.2 6-4.2v-.4z" fill-rule="evenodd"/></svg>
      </div>
      <div class="contact-line contact-address">
        <span>Corner of Brisco Avenue and Velhurst Street</span>
        <svg viewBox="0 0 16 16" aria-hidden="true"><path d="M8 1l7 6.5h-2V15H9.5v-4.5h-3V15H3V7.5H1z"/></svg>
      </div>
      <div class="contact-line">
        <span>Makati City, Philippines</span>
        <span class="icon-spacer"></span>
      </div>
    </address>
  </article>
</main>
</body>
</html>
```